Professional
Mark Elwood
President
4217 Vista Arroyo Place, NW
Albuquerque, NM 87114
melwood@emibq.com
www.emibq.com
New Construction*Remodels* Renovations*Handyman Services
Here is my logo for the stationary and business cards
Logo .AI file

```html
<!DOCTYPE html>
<html lang="en">
<head>
<meta charset="utf-8">
<title>Elwood Masonry, Inc. — Stationery Set</title>
<link href="https://fonts.googleapis.com/css2?family=Roboto+Condensed:wght@700&family=Open+Sans:wght@400;600&display=swap" rel="stylesheet">
<style>
  :root{
    --red:#d3192b;
    --red-dark:#a60f1d;
    --black:#1c1c1c;
    --grey:#8a8a8a;
    --paper:#ffffff;
    --stage:#e9e6e1;
    --faint:#f1e9e9;
  }
  *{box-sizing:border-box;margin:0;padding:0}
  html,body{width:1200px;height:310px;overflow:hidden}
  body{background:var(--stage);position:relative;font-family:"Open Sans",sans-serif;color:var(--black)}
  .piece{position:absolute;background:var(--paper);box-shadow:0 2px 5px rgba(0,0,0,.25);overflow:hidden}
  .brand{display:flex;align-items:center;gap:4px;font-family:"Roboto Condensed",sans-serif;font-weight:700;color:var(--black);white-space:nowrap;line-height:1}
  .brand::before{content:"";flex:none;border-radius:50%;background:var(--red)}
  .brand--xl{font-size:17px}.brand--xl::before{width:34px;height:34px}
  .brand--sm{font-size:7px}.brand--sm::before{width:11px;height:11px}
  .brand--xs{font-size:5px}.brand--xs::before{width:8px;height:8px}
  .brand--white{color:#fff}.brand--white::before{background:#fff}
  .tiny{font-size:3.4px;line-height:1.45;color:#444}
  .swoosh{position:absolute;right:0;bottom:0}
  .showcase-logo{left:14px;top:62px;position:absolute}
  .showcase-logo .tagline{font-size:5px;color:var(--grey);margin:4px 0 0 38px}
  /* business cards */
  .card{width:106px;height:62px}
  .card .brand{position:absolute;left:8px;top:22px}
  .card .contact{position:absolute;right:6px;top:14px;text-align:right}
  .card .name{font-weight:600;font-size:5px;color:var(--black)}
  .card--red{background:var(--red)}
  /* letterhead */
  .letterhead{width:164px;height:252px}
  .letterhead .brand{position:absolute;left:10px;top:12px}
  .letterhead .contact{position:absolute;right:10px;top:12px;text-align:right}
  .watermark{position:absolute;left:32px;top:86px;width:100px;height:100px;border-radius:50%;background:var(--faint);display:flex;align-items:center;justify-content:center;font-family:"Roboto Condensed",sans-serif;font-weight:700;font-size:10px;color:#ead8d8}
  /* envelopes */
  .envelope{width:200px;height:84px}
  .envelope .brand{position:absolute;left:8px;top:8px}
  .envelope .contact{position:absolute;left:8px;top:22px}
  .window{position:absolute;left:30px;top:44px;width:70px;height:22px;border:1px solid #ddd;border-radius:2px}
  .envelope-back{width:330px;height:76px}
  .envelope-back svg{position:absolute;inset:0}
  .envelope-back .brand{position:absolute;left:50%;transform:translateX(-50%)}
</style>
</head>
<body>

<div class="showcase-logo">
  <div class="brand brand--xl">ELWOOD MASONRY, INC.</div>
  <p class="tagline">New Construction • Remodels • Renovations • Handyman Services</p>
</div>

<!-- business cards -->
<div class="piece card" style="left:12px;top:126px">
  <div class="brand brand--sm">ELWOOD MASONRY, INC.</div>
  <svg class="swoosh" width="40" height="16" viewBox="0 0 40 16"><polygon points="8,16 40,2 40,16" fill="var(--red)"/><polygon points="0,16 40,10 40,16" fill="var(--black)"/></svg>
</div>
<div class="piece card" style="left:126px;top:126px">
  <div class="contact tiny">
    <p class="name">Mark Elwood</p>
    <p>President</p>
    <p>4217 Vista Arroyo Place, NW</p>
    <p>Albuquerque, NM 87114</p>
    <p>Phone (505) 555-0142</p>
    <p>melwood@emibq.com</p>
    <p>www.emibq.com</p>
  </div>
  <svg class="swoosh" width="106" height="10" viewBox="0 0 106 10"><polygon points="0,10 0,4 106,0 106,10" fill="var(--red)"/></svg>
</div>
<div class="piece card" style="left:12px;top:196px">
  <div class="brand brand--sm">ELWOOD MASONRY, INC.</div>
  <svg class="swoosh" width="106" height="8" viewBox="0 0 106 8"><rect width="106" height="8" fill="var(--black)"/></svg>
</div>
<div class="piece card card--red" style="left:126px;top:196px">
  <div class="brand brand--sm brand--white">ELWOOD MASONRY, INC.</div>
</div>

<!-- letterheads -->
<div class="piece letterhead" style="left:262px;top:30px">
  <div class="brand brand--xs">ELWOOD MASONRY, INC.</div>
  <div class="contact tiny">
    <p>4217 Vista Arroyo Place, NW</p>
    <p>Albuquerque, NM 87114</p>
    <p>Office (505) 555-0142</p>
    <p>www.emibq.com</p>
  </div>
  <div class="watermark" role="img" aria-label="Faint company name watermark">ELWOOD</div>
  <svg class="swoosh" width="70" height="22" viewBox="0 0 70 22"><polygon points="10,22 70,2 70,22" fill="var(--red)"/><polygon points="0,22 70,14 70,22" fill="var(--black)"/></svg>
</div>
<div class="piece letterhead" style="left:442px;top:30px">
  <div class="brand brand--xs">ELWOOD MASONRY, INC.</div>
  <div class="contact tiny">
    <p>4217 Vista Arroyo Place, NW</p>
    <p>Albuquerque, NM 87114</p>
    <p>Fax (505) 555-0187</p>
    <p>melwood@emibq.com</p>
  </div>
  <div class="watermark" role="img" aria-label="Faint company name watermark">ELWOOD</div>
  <svg class="swoosh" width="70" height="22" viewBox="0 0 70 22"><polygon points="10,22 70,2 70,22" fill="var(--red)"/><polygon points="0,22 70,14 70,22" fill="var(--black)"/></svg>
</div>

<!-- envelopes front -->
<div class="piece envelope" style="left:628px;top:36px">
  <div class="brand brand--xs">ELWOOD MASONRY, INC.</div>
  <div class="contact tiny"><p>4217 Vista Arroyo Place, NW</p><p>Albuquerque, NM 87114</p></div>
  <svg class="swoosh" width="60" height="14" viewBox="0 0 60 14"><polygon points="8,14 60,2 60,14" fill="var(--red)"/><polygon points="0,14 60,9 60,14" fill="var(--black)"/></svg>
</div>
<div class="piece envelope" style="left:628px;top:176px">
  <div class="brand brand--xs">ELWOOD MASONRY, INC.</div>
  <div class="contact tiny"><p>4217 Vista Arroyo Place, NW</p><p>Albuquerque, NM 87114</p></div>
  <div class="window"></div>
  <svg class="swoosh" width="60" height="14" viewBox="0 0 60 14"><polygon points="8,14 60,2 60,14" fill="var(--red)"/><polygon points="0,14 60,9 60,14" fill="var(--black)"/></svg>
</div>

<!-- envelope backs -->
<div class="piece envelope-back" style="left:850px;top:30px">
  <svg viewBox="0 0 330 76" preserveAspectRatio="none"><polygon points="0,0 330,0 330,30 165,50 0,30" fill="var(--red)"/><polygon points="0,0 330,0 330,8 0,8" fill="var(--black)"/></svg>
  <div class="brand brand--xs brand--white" style="top:30px">ELWOOD</div>
</div>
<div class="piece envelope-back" style="left:850px;top:120px">
  <svg viewBox="0 0 330 76" preserveAspectRatio="none"><polyline points="0,0 165,42 330,0" fill="none" stroke="#ddd" stroke-width="1"/><polygon points="150,38 165,42 180,38 165,48" fill="var(--red)"/></svg>
</div>
<div class="piece envelope-back" style="left:850px;top:210px">
  <svg viewBox="0 0 330 76" preserveAspectRatio="none"><polyline points="0,0 165,34 330,0" fill="none" stroke="#ddd" stroke-width="1"/><polyline points="0,76 165,40 330,76" fill="none" stroke="#e6e6e6" stroke-width="1"/></svg>
  <div class="brand brand--xs" style="top:30px">ELWOOD</div>
</div>

</body>
</html>
```